website design for Company MVR

Our company name MVR(the grand mural limited), need design a website. It is a website that focuses on promoting art design in the world.
We will provide the existing logo design, the new website and logo should be matched to each other. The website has to include pages "Home" "Contact" "Service" and So on at least 6-8 pages. The site is mainly for publicity and promotion. We will have an existing domain and hosting.
Updates

We prefer the original design, thanks.

Target Market(s)

large public art

Industry/Entity Type

Architecture and design, large public art and sculpture manufacturer

Coding

Coded - Design and coding required

Number of Pages Required

5+ page

Requirements
Must have
• 1. the overall color has to match our logo color 2. Do not need to do any change on our logo including the color 3. Here is a similar style of the home page we like, it can be similar but must not same. Pls check the below link. https://www.velmardo.it/en-us/

```html
<!DOCTYPE html>
<html lang="en">
<head>
<meta charset="utf-8">
<title>MVR — The Grand Mural</title>
<link href="https://fonts.googleapis.com/css2?family=Poppins:wght@300;400;500;600;700;800&family=Lexend:wght@400;500;600&display=swap" rel="stylesheet">
<style>
:root{
  --ink:#231f20;
  --paper:#ffffff;
  --mist:#f1f1f1;
  --tile:#e6e6e6;
  --muted:#7a7a7a;
  --footer:#1d1d1d;
  --bar:#5b5b5b;
  --star:#f4a21b;
}
*{margin:0;padding:0;box-sizing:border-box}
html,body{width:1200px;height:5376px;overflow:hidden}
body{position:relative;background:var(--paper);font-family:"Poppins",sans-serif;color:var(--ink)}
.abs{position:absolute}
.heading{font-family:"Lexend",sans-serif;font-weight:500;color:var(--ink)}
.body-text{font-size:11.5px;line-height:20px;color:#555}
.fill{display:block}
.btn{position:absolute;display:flex;align-items:center;gap:8px}
.btn span{background:var(--ink);color:#fff;font-size:12px;font-weight:600;letter-spacing:.5px;padding:0 20px;height:34px;line-height:34px}
.marker{position:absolute;width:14px;height:64px}

/* header */
.site-header{left:0;top:0;width:1200px;height:75px;background:#fff;border-bottom:1px solid #eee}
.brand{left:60px;top:24px;display:flex;align-items:center;gap:10px}
.brand-square{width:14px;height:14px;background:var(--ink)}
.brand-name{font-weight:600;font-size:22px;line-height:26px;color:var(--ink)}
.nav{left:540px;top:30px;display:flex;gap:26px;font-size:12px;color:#777}
.nav .active{color:var(--ink);font-weight:500}
.nav-icons{left:990px;top:22px;display:flex;gap:8px}
.nav-icons span{width:30px;height:30px;border:2px solid var(--ink);border-radius:50%;display:flex;align-items:center;justify-content:center}

/* hero */
.hero{left:0;top:75px;width:1200px;height:635px;background:var(--mist);overflow:hidden}
.hero-title{left:365px;top:175px;font-weight:800;font-size:58px;line-height:76px;letter-spacing:4px;color:var(--ink)}

/* about */
.about-box{left:202px;top:818px;width:420px;height:447px;border:5px solid #a9a9a9}
.about-list{list-style:none;font-size:11.5px;color:#555}
.about-list li{display:flex;align-items:center;gap:12px;height:30px}

/* collections */
.collections{left:0;top:1402px;width:1200px;height:904px;background:var(--mist)}
.tile{position:absolute;background:var(--tile)}
.tile-art{position:absolute;border:8px solid #fff;box-shadow:0 2px 6px rgba(0,0,0,.2)}
.tile-label{position:absolute;font-size:17px;font-weight:600;color:var(--ink)}

.artist-name{font-size:14px;font-weight:600;text-align:center}
.artist-role{font-size:11px;color:var(--muted);text-align:center;margin-top:4px}

.testimonials{left:0;top:3819px;width:1200px;height:397px;background:#f7f7f7}

.event-card{position:absolute;width:292px;height:320px}
.event-name{font-size:14px;font-weight:600}
.event-role{font-size:11px;color:var(--muted)}

.footer{left:0;top:5013px;width:1200px;height:326px;background:var(--footer);color:#fff}
.footer h4{font-size:15px;font-weight:500;margin-bottom:10px}
.footer ul{list-style:none;font-size:11.5px;color:#bbb;line-height:22px}
.copyright{left:0;top:5339px;width:1200px;height:37px;background:var(--bar);color:#eee;font-size:11px;text-align:center;line-height:37px}
.input{position:absolute;height:36px;border:1px solid #ccc;font-size:11px;color:#777;padding-left:10px;line-height:34px}
</style>
</head>
<body>

<header class="abs site-header">
  <div class="abs brand"><span class="brand-square"></span><span class="brand-name">MVR The Grand Mural</span></div>
  <nav class="abs nav">
    <span class="active">Home</span><span>Artworks</span><span>Collections</span><span>Live</span><span>Artist</span><span>Events</span><span class="active">EN ▾</span>
  </nav>
  <div class="abs" style="left:546px;top:56px;width:22px;height:2px;background:var(--ink)"></div>
  <div class="abs nav-icons">
    <span><svg width="14" height="14" viewBox="0 0 14 14"><circle cx="6" cy="6" r="4.5" fill="none" stroke="#231f20" stroke-width="2"/><path d="M9.5 9.5 L13 13" stroke="#231f20" stroke-width="2"/></svg></span>
    <span><svg width="14" height="14" viewBox="0 0 14 14"><circle cx="7" cy="5" r="3" fill="none" stroke="#231f20" stroke-width="1.6"/><path d="M1.5 13 C2.5 9 11.5 9 12.5 13" fill="none" stroke="#231f20" stroke-width="1.6"/></svg></span>
    <span><svg width="14" height="14" viewBox="0 0 14 14"><rect x="2" y="5" width="10" height="8" fill="none" stroke="#231f20" stroke-width="1.6"/><path d="M4.5 5 V3.5 a2.5 2.5 0 0 1 5 0 V5" fill="none" stroke="#231f20" stroke-width="1.6"/></svg></span>
    <span><svg width="14" height="14" viewBox="0 0 14 14"><path d="M7 12.5 L1.8 7.3 A3 3 0 0 1 7 3.2 A3 3 0 0 1 12.2 7.3 Z" fill="none" stroke="#231f20" stroke-width="1.6"/></svg></span>
  </div>
</header>

<section class="abs hero">
  <div class="abs fill" role="img" aria-label="Violet and magenta ink swirl artwork" style="left:0;top:134px;width:330px;height:316px;background:linear-gradient(135deg,#2a1f2d,#a23a7a 45%,#3b2a45)"></div>
  <div class="abs fill" role="img" aria-label="Black and white street mural artwork" style="left:760px;top:44px;width:440px;height:528px;background:linear-gradient(135deg,#3a3a3e,#c9c9cc 50%,#55555a)"></div>
  <div class="abs" style="left:599px;top:585px;width:2px;height:75px;background:var(--ink)"></div>
  <div class="abs hero-title">THE<br>GRAND MURAL</div>
  <div class="btn" style="left:365px;top:342px"><span>CONTACT US</span>
    <svg width="26" height="16" viewBox="0 0 26 16"><path d="M1 8 H23 M16 1 L24 8 L16 15" fill="none" stroke="#231f20" stroke-width="2.2"/></svg></div>
</section>

<section>
  <div class="abs" style="left:830px;top:1000px;width:240px;height:270px;background:#ececec"></div>
  <div class="abs about-box"></div>
  <svg class="marker" style="left:230px;top:826px" viewBox="0 0 14 64"><line x1="7" y1="0" x2="7" y2="54" stroke="#231f20" stroke-width="1.5"/><circle cx="7" cy="58" r="5" fill="#231f20"/></svg>
  <h2 class="abs heading" style="left:265px;top:890px;font-size:40px">About Us</h2>
  <p class="abs body-text" style="left:263px;top:948px;width:305px">Lorem Ipsum is simply dummy text of the printing and typesetting industry. Lorem Ipsum has been the industry's standard dummy text ever since the 1500s, when an unknown .</p>
  <ul class="abs about-list" style="left:262px;top:1042px">
    <li><svg width="14" height="12" viewBox="0 0 14 12"><path d="M1 6 L5 10 L13 2" fill="none" stroke="#231f20" stroke-width="1.8"/></svg>There are many variations</li>
    <li><svg width="14" height="12" viewBox="0 0 14 12"><path d="M1 6 L5 10 L13 2" fill="none" stroke="#231f20" stroke-width="1.8"/></svg>There are many variations</li>
    <li><svg width="14" height="12" viewBox="0 0 14 12"><path d="M1 6 L5 10 L13 2" fill="none" stroke="#231f20" stroke-width="1.8"/></svg>There are many variations</li>
  </ul>
  <div class="btn" style="left:262px;top:1150px"><span>CONTACT US</span>
    <svg width="26" height="16" viewBox="0 0 26 16"><path d="M1 8 H23 M16 1 L24 8 L16 15" fill="none" stroke="#231f20" stroke-width="2.2"/></svg></div>
  <div class="abs fill" role="img" aria-label="Purple wall mural of a woman reading" style="left:630px;top:845px;width:336px;height:292px;background:linear-gradient(135deg,#6b3fa0,#9a5cc2 45%,#3d7aa8)"></div>
  <div class="abs fill" role="img" aria-label="Classical painting of cherubs carrying a barrel" style="left:538px;top:1114px;width:263px;height:188px;background:linear-gradient(135deg,#b9a68a,#d9c3a6 50%,#8d7a63);border:4px solid #fff"></div>
</section>

<section class="abs collections">
  <svg class="marker" style="left:438px;top:8px" viewBox="0 0 14 64"><line x1="7" y1="0" x2="7" y2="54" stroke="#231f20" stroke-width="1.5"/><circle cx="7" cy="58" r="5" fill="#231f20"/></svg>
  <h2 class="abs heading" style="left:472px;top:72px;font-size:38px">Collections</h2>

  <div class="abs fill" role="img" aria-label="Landscape painting of blue sky over dark hills" style="left:60px;top:147px;width:528px;height:300px;background:linear-gradient(180deg,#3aa7e0,#bfe4f5 32%,#3b3426 45%,#2c281d)"></div>
  <div class="tile-label" style="left:60px;top:456px">Landscap</div>
  <div class="abs" style="left:60px;top:481px;width:528px;height:2px;background:var(--ink)"></div>

  <div class="tile" style="left:611px;top:147px;width:253px;height:300px"><div class="tile-art fill" role="img" aria-label="Portrait in a round ornate frame" style="left:36px;top:36px;width:181px;height:226px;background:radial-gradient(circle,#7b8a5c,#e8dcc0 60%,#f5efe3)"></div></div>
  <div class="tile-label" style="left:611px;top:456px">Abstract</div>
  <div class="tile" style="left:887px;top:147px;width:253px;height:300px"><div class="tile-art fill" role="img" aria-label="Colourful pop art portrait with flowers" style="left:36px;top:36px;width:181px;height:226px;background:linear-gradient(135deg,#29a8d8,#e9e9e9 50%,#d6334a)"></div></div>
  <div class="tile-label" style="left:887px;top:456px">Nature</div>

  <div class="tile" style="left:60px;top:514px;width:253px;height:300px"><div class="tile-art fill" role="img" aria-label="Vintage illustrated portrait" style="left:36px;top:36px;width:181px;height:226px;background:linear-gradient(135deg,#4f6a4a,#c9b27a 55%,#7a4a2c)"></div></div>
  <div class="tile-label" style="left:60px;top:823px">Portrait</div>
  <div class="tile" style="left:336px;top:514px;width:253px;height:300px"><div class="tile-art fill" role="img" aria-label="Classical painting with figures in red" style="left:36px;top:36px;width:181px;height:226px;background:linear-gradient(135deg,#8c2a1e,#c2402e 50%,#d8a15c)"></div></div>
  <div class="tile-label" style="left:336px;top:823px">Ubran</div>
  <div class="tile" style="left:611px;top:514px;width:253px;height:300px"><div class="tile-art fill" role="img" aria-label="Street art portrait with red lettering" style="left:36px;top:36px;width:181px;height:226px;background:linear-gradient(135deg,#5d4d42,#b08b6f 50%,#c03b3b)"></div></div>
  <div class="tile-label" style="left:611px;top:823px">PopCluture</div>
  <div class="tile" style="left:887px;top:514px;width:253px;height:300px"><div class="tile-art fill" role="img" aria-label="Vivid watercolour face with splashes of colour" style="left:36px;top:36px;width:181px;height:226px;background:linear-gradient(135deg,#f4d12e,#e85aa1 45%,#3ab0d9)"></div></div>
  <div class="tile-label" style="left:887px;top:823px">Every Day</div>
</section>

<section>
  <svg class="marker" style="left:94px;top:2314px" viewBox="0 0 14 64"><line x1="7" y1="0" x2="7" y2="54" stroke="#231f20" stroke-width="1.5"/><circle cx="7" cy="58" r="5" fill="#231f20"/></svg>
  <h2 class="abs heading" style="left:125px;top:2366px;font-size:34px;line-height:42px;font-weight:400">latest collections of<br>original artworks &amp;<br>paintings</h2>
  <p class="abs body-text" style="left:780px;top:2372px;width:360px;text-align:right">Lorem Ipsum is simply dummy text of the printing and typesetting industry. Lorem Ipsum has been the industry's</p>
  <svg class="abs" style="left:1062px;top:2428px" width="80" height="36" viewBox="0 0 80 36">
    <circle cx="17" cy="18" r="15" fill="none" stroke="#231f20" stroke-width="1.5"/><path d="M20 11 L13 18 L20 25" fill="none" stroke="#231f20" stroke-width="1.8"/>
    <circle cx="61" cy="18" r="15" fill="none" stroke="#231f20" stroke-width="1.5"/><path d="M58 11 L65 18 L58 25" fill="none" stroke="#231f20" stroke-width="1.8"/>
  </svg>
  <div class="abs fill" role="img" aria-label="Pastoral painting with figures under trees" style="left:0;top:2515px;width:230px;height:170px;background:linear-gradient(135deg,#6d7d4a,#b8b07a 50%,#3e4a2e)"></div>
  <div class="abs fill" role="img" aria-label="Geometric stained-glass style mural" style="left:328px;top:2515px;width:330px;height:236px;background:linear-gradient(135deg,#2e8a4a,#d6a33a 40%,#c23a3a 70%,#2a2a2a)"></div>
  <div class="abs fill" role="img" aria-label="Colourful abstract painting" style="left:755px;top:2515px;width:187px;height:163px;background:linear-gradient(135deg,#2f7fd0,#f07b3a 50%,#f2c1d5)"></div>
  <div class="abs fill" role="img" aria-label="Pastel bubbles abstract artwork" style="left:1016px;top:2515px;width:184px;height:163px;background:linear-gradient(135deg,#d567c9,#f1c04a 50%,#3fb4d8)"></div>
</section>

<section>
  <div class="abs" style="left:60px;top:2874px;width:600px;height:432px;background:#e7e7e7"></div>
  <div class="abs" style="left:182px;top:2924px;width:150px;height:150px;background:#fff;border:5px solid var(--ink)"><div class="abs fill" role="img" aria-label="Dark classical interior painting" style="left:26px;top:26px;width:88px;height:88px;background:linear-gradient(135deg,#3a2a1e,#8a6a45)"></div></div>
  <div class="abs" style="left:361px;top:2924px;width:150px;height:150px;background:#fff;border:5px solid var(--ink)"><div class="abs fill" role="img" aria-label="Ink drawing of a bird on a branch" style="left:26px;top:26px;width:88px;height:88px;background:linear-gradient(135deg,#ece6da,#cfc3ad)"></div></div>
  <div class="abs" style="left:182px;top:3097px;width:150px;height:150px;background:#fff;border:5px solid var(--ink)"><div class="abs fill" role="img" aria-label="Illustration of a figure in pink on blue" style="left:26px;top:26px;width:88px;height:88px;background:linear-gradient(135deg,#7aa6d6,#e08a6a)"></div></div>
  <div class="abs" style="left:361px;top:3097px;width:150px;height:150px;background:#fff;border:5px solid var(--ink)"><div class="abs fill" role="img" aria-label="Bold colourful pop portrait" style="left:26px;top:26px;width:88px;height:88px;background:linear-gradient(135deg,#2a5cc8,#f2c23a 50%,#d2333f)"></div></div>
  <svg class="marker" style="left:687px;top:2850px" viewBox="0 0 14 64"><line x1="7" y1="0" x2="7" y2="54" stroke="#231f20" stroke-width="1.5"/><circle cx="7" cy="58" r="5" fill="#231f20"/></svg>
  <h2 class="abs heading" style="left:720px;top:2904px;font-size:34px">Upcoming Exhibitions</h2>
  <p class="abs body-text" style="left:720px;top:2956px;width:330px">Lorem Ipsum is simply dummy text of the printing and typesetting industry. Lorem Ipsum has been the industry's</p>
  <div class="abs" style="left:720px;top:3024px;font-size:14px;font-weight:500">3, Dec</div>
  <div class="abs" style="left:720px;top:3055px;font-size:18px;font-weight:600">The Test Of Art</div>
  <p class="abs body-text" style="left:720px;top:3080px;width:370px">It is a long established fact that a reader will be distracted by the readable content of a page when looking at its layout. The point of using Lorem Ipsum is that it has a more-or-less normal distribution of letters, as opposed to using 'Content here, content here', making it look like readable English.</p>
  <div class="btn" style="left:720px;top:3218px"><span>VIEW MORE</span>
    <svg width="26" height="16" viewBox="0 0 26 16"><path d="M1 8 H23 M16 1 L24 8 L16 15" fill="none" stroke="#231f20" stroke-width="2.2"/></svg></div>
</section>

<section>
  <svg class="marker" style="left:420px;top:3362px" viewBox="0 0 14 64"><line x1="7" y1="0" x2="7" y2="54" stroke="#231f20" stroke-width="1.5"/><circle cx="7" cy="58" r="5" fill="#231f20"/></svg>
  <h2 class="abs heading" style="left:458px;top:3392px;font-size:34px">Artists Collectors</h2>
  <div class="abs" style="left:150px;top:3458px;width:194px"><div class="fill" role="img" aria-label="Photo of an artist in a dark suit" style="height:225px;background:linear-gradient(180deg,#d9d9d9,#7a6e69 55%,#2b2424);border-bottom:6px solid #cfcfcf"></div><div class="artist-name" style="margin-top:26px">Artist Name</div><div class="artist-role">United Kingdom - Painter</div></div>
  <div class="abs" style="left:375px;top:3458px;width:194px"><div class="fill" role="img" aria-label="Photo of an artist painting a wall" style="height:225px;background:linear-gradient(180deg,#8a9a86,#5a4e44 55%,#2b2b2b);border-bottom:6px solid #cfcfcf"></div><div class="artist-name" style="margin-top:26px">Artist Name</div><div class="artist-role">United Kingdom - Painter</div></div>
  <div class="abs" style="left:600px;top:3458px;width:194px"><div class="fill" role="img" aria-label="Photo of an artist seated in a studio" style="height:225px;background:linear-gradient(180deg,#3a3236,#7a5a4a 55%,#2a2222);border-bottom:6px solid #cfcfcf"></div><div class="artist-name" style="margin-top:26px">Artist Name</div><div class="artist-role">United Kingdom - Painter</div></div>
  <div class="abs" style="left:825px;top:3458px;width:194px"><div class="fill" role="img" aria-label="Photo of an artist sketching at a table" style="height:225px;background:linear-gradient(180deg,#bdbdbd,#e8e2dc 55%,#9a9a9a);border-bottom:6px solid #cfcfcf"></div><div class="artist-name" style="margin-top:26px">Artist Name</div><div class="artist-role">United Kingdom - Painter</div></div>
</section>

<section class="abs testimonials">
  <svg class="marker" style="left:64px;top:12px" viewBox="0 0 14 64"><line x1="7" y1="0" x2="7" y2="54" stroke="#231f20" stroke-width="1.5"/><circle cx="7" cy="58" r="5" fill="#231f20"/></svg>
  <h2 class="abs heading" style="left:102px;top:44px;font-size:34px">Testimonials</h2>
  <svg class="abs" style="left:60px;top:110px" width="92" height="60" viewBox="0 0 92 60"><path d="M2 58 V30 C2 12 14 3 30 2 V14 C20 16 16 22 16 28 H38 V58 Z M50 58 V30 C50 12 62 3 78 2 V14 C68 16 64 22 64 28 H86 V58 Z" fill="#c9c9c9"/></svg>
  <p class="abs body-text" style="left:62px;top:176px;width:330px">Lorem Ipsum is simply dummy text of the printing and typesetting industry. Lorem Ipsum has been the industry's standard dummy text ever since the 1500s,</p>
  <div class="abs" style="left:62px;top:256px;font-size:14px;font-weight:600">Artist Name</div>
  <div class="abs" style="left:62px;top:278px;font-size:11px;color:var(--muted)">United Kingdom - Painter</div>
  <div class="abs" style="left:60px;top:295px;font-size:13px;color:var(--star);letter-spacing:2px">★★★★★</div>
  <div class="abs fill" role="img" aria-label="Small botanical print" style="left:616px;top:263px;width:66px;height:66px;background:linear-gradient(135deg,#efe8da,#c6b28a);border:2px solid #fff;box-shadow:0 1px 4px rgba(0,0,0,.25)"></div>
  <div class="abs fill" role="img" aria-label="Small misty landscape print" style="left:690px;top:263px;width:66px;height:66px;background:linear-gradient(135deg,#7f95a8,#4a5a64)"></div>
  <div class="abs fill" role="img" aria-label="Small blue night artwork" style="left:764px;top:263px;width:66px;height:66px;background:linear-gradient(135deg,#1e2a6a,#d04a3a)"></div>
  <div class="abs" style="left:853px;top:75px;width:248px;height:248px;background:var(--ink)"></div>
  <div class="abs fill" role="img" aria-label="Watercolour portrait in pink and red tones" style="left:839px;top:89px;width:248px;height:248px;background:linear-gradient(135deg,#e8456a,#f4b2c1 45%,#3aa5c8 80%,#f2cf4a)"></div>
</section>

<section>
  <svg class="marker" style="left:440px;top:4240px" viewBox="0 0 14 64"><line x1="7" y1="0" x2="7" y2="54" stroke="#231f20" stroke-width="1.5"/><circle cx="7" cy="58" r="5" fill="#231f20"/></svg>
  <h2 class="abs heading" style="left:480px;top:4294px;font-size:36px">Events</h2>
  <div class="event-card" style="left:119px;top:4366px">
    <div class="abs" style="left:0;top:0;width:18px;height:230px;border-left:2px solid #888;border-top:2px solid #888"></div>
    <div class="abs fill" role="img" aria-label="Black and white sketch artwork" style="left:10px;top:8px;width:282px;height:150px;background:linear-gradient(135deg,#4a5a6a,#cfd4d8 55%,#2a2a2a)"></div>
    <div class="abs" style="left:40px;top:170px;width:20px;height:2px;background:var(--ink)"></div>
    <div class="abs event-name" style="left:88px;top:162px">Event Name</div>
    <div class="abs event-role" style="left:88px;top:184px">United Kingdom - Painter</div>
    <p class="abs body-text" style="left:88px;top:212px;width:180px">Lorem Ipsum is simply dummy text of the printing and typesetting industry.</p>
    <div class="abs" style="left:228px;top:230px;width:64px;height:70px;border-right:6px solid #e5e5e5;border-bottom:6px solid #e5e5e5"></div>
  </div>
  <div class="event-card" style="left:457px;top:4366px">
    <div class="abs" style="left:0;top:0;width:18px;height:230px;border-left:2px solid #888;border-top:2px solid #888"></div>
    <div class="abs fill" role="img" aria-label="Dripping neon painted artwork" style="left:10px;top:8px;width:282px;height:150px;background:linear-gradient(135deg,#d43a8a,#f2d23a 40%,#2aa0d8 70%,#2a2a2a)"></div>
    <div class="abs" style="left:40px;top:170px;width:20px;height:2px;background:var(--ink)"></div>
    <div class="abs event-name" style="left:88px;top:162px">Event Name</div>
    <div class="abs event-role" style="left:88px;top:184px">United Kingdom - Painter</div>
    <p class="abs body-text" style="left:88px;top:212px;width:180px">Lorem Ipsum is simply dummy text of the printing and typesetting industry.</p>
    <div class="abs" style="left:228px;top:230px;width:64px;height:70px;border-right:6px solid #e5e5e5;border-bottom:6px solid #e5e5e5"></div>
  </div>
  <div class="event-card" style="left:795px;top:4366px">
    <div class="abs" style="left:0;top:0;width:18px;height:230px;border-left:2px solid #888;border-top:2px solid #888"></div>
    <div class="abs fill" role="img" aria-label="Baroque ceiling painting" style="left:10px;top:8px;width:282px;height:150px;background:linear-gradient(135deg,#7a8aa0,#d8c3a0 50%,#8a5a3a)"></div>
    <div class="abs" style="left:40px;top:170px;width:20px;height:2px;background:var(--ink)"></div>
    <div class="abs event-name" style="left:88px;top:162px">Event Name</div>
    <div class="abs event-role" style="left:88px;top:184px">United Kingdom - Painter</div>
    <p class="abs body-text" style="left:88px;top:212px;width:180px">Lorem Ipsum is simply dummy text of the printing and typesetting industry.</p>
    <div class="abs" style="left:228px;top:230px;width:64px;height:70px;border-right:6px solid #e5e5e5;border-bottom:6px solid #e5e5e5"></div>
  </div>
</section>

<section>
  <div class="abs" style="left:0;top:4754px;width:1200px;height:259px;background:#f4f4f4"></div>
  <div class="abs fill" role="img" aria-label="Red and black marbled paint artwork" style="left:0;top:4754px;width:230px;height:259px;background:linear-gradient(135deg,#1f1a1a,#d2563f 40%,#f0c6b5 60%,#3a2020)"></div>
  <div class="abs" style="left:219px;top:4796px;width:747px;height:192px;background:#fff"></div>
  <svg class="marker" style="left:358px;top:4752px" viewBox="0 0 14 64"><line x1="7" y1="0" x2="7" y2="54" stroke="#231f20" stroke-width="1.5"/><circle cx="7" cy="58" r="5" fill="#231f20"/></svg>
  <h2 class="abs heading" style="left:386px;top:4822px;font-size:36px">Subsribe Newsletter</h2>
  <div class="input" style="left:236px;top:4884px;width:259px">Name *</div>
  <div class="input" style="left:507px;top:4884px;width:259px">Email *</div>
  <div class="btn" style="left:776px;top:4885px"><span style="padding:0 30px">SUSCRIBE</span>
    <svg width="26" height="16" viewBox="0 0 26 16"><path d="M1 8 H23 M16 1 L24 8 L16 15" fill="none" stroke="#231f20" stroke-width="2.2"/></svg></div>
</section>

<footer class="abs footer">
  <div class="abs" style="left:62px;top:74px;display:flex;align-items:center;gap:10px">
    <span style="width:12px;height:12px;background:#fff"></span>
    <span style="font-weight:600;font-size:18px;line-height:22px">MVR The Grand Mural</span>
  </div>
  <div class="abs" style="left:338px;top:66px"><h4>Site Map</h4><ul><li>- Home</li><li>- About Us</li><li>- Exebution</li><li>- Artworks</li><li>- Collection</li><li>- Artist</li><li>- Event</li><li>- Contact Us</li></ul></div>
  <div class="abs" style="left:611px;top:66px"><h4>Resources</h4><ul><li>- Open source</li><li>- Blog</li><li>- The Art Project</li><li>- Printing</li><li>- Education</li></ul></div>
  <div class="abs" style="left:887px;top:66px"><h4>Follow Us</h4>
    <svg width="150" height="36" viewBox="0 0 150 36"><g fill="none" stroke="#fff" stroke-width="1.6"><circle cx="16" cy="18" r="15"/><circle cx="54" cy="18" r="15"/><circle cx="92" cy="18" r="15"/><circle cx="130" cy="18" r="15"/></g></svg>
  </div>
</footer>
<div class="abs copyright">© 2021 The Grand Mural - All Right Reserved.</div>

</body>
</html>
```